Modern business card design for professional copywriter

I'd like a business card design that I can use to have my cards printed out by plink.com as a squared corners business card (see artwork and design guidelines here: https://help.plink.com/hc/en-gb/sections/300481726-PLINK-Product-Templates)

The design should be clean and modern and reflect the colours, tone and branding on my website: https://noravestrel.com.au

Target Market(s)

Professionals, B2B small business owners

Industry/Entity Type

Business

Contact Information for Business Card

Nora Vestrel
m: 0427 593 864
e: nora@noravestrel.com.au
w: noravestrel.com.au

Font styles to use
Sans Serif

Requirements
Must have
• Tagline: "Smart copywriting for clever business people"
• Brand colours: fd8000, 009984, 666666 and black
Nice to have

```html
<!DOCTYPE html>
<html lang="en">
<head>
<meta charset="utf-8">
<title>Nora Vestrel – Business Card</title>
<link rel="stylesheet" href="https://fonts.googleapis.com/css2?family=Arimo:wght@400;700&family=Questrial&display=swap">
<style>
  :root {
    --bg: #dfe5e6;
    --card: #ffffff;
    --orange: #fd8000;
    --green: #2fb36c;
    --grey: #666666;
    --ink: #111111;
    --photo-light: #e6dcd2;
    --photo-dark: #8a8580;
  }
  * { box-sizing: border-box; margin: 0; padding: 0; }
  html, body {
    width: 1200px; height: 1200px; overflow: hidden;
    background: var(--bg);
  }
  .canvas {
    width: 1200px; height: 1200px;
    display: flex; flex-direction: column;
    align-items: center; justify-content: center; gap: 70px;
  }
  .card {
    position: relative;
    width: 640px; height: 391px;
    background: var(--card);
    box-shadow: 0 10px 28px rgba(60, 80, 85, 0.18);
  }
  /* Front */
  .card--front {
    display: flex; flex-direction: column;
    align-items: center; justify-content: center;
  }
  .brand {
    display: flex; align-items: center; gap: 12px;
    margin-top: -20px;
  }
  .brand__mark {
    width: 22px; height: 22px;
    background: var(--green);
  }
  .brand__name {
    font-family: "Questrial", sans-serif;
    font-size: 46px; color: var(--orange);
    letter-spacing: 0.5px;
  }
  .tagline {
    margin-top: 64px;
    font-family: "Arimo", sans-serif;
    font-weight: 700; font-size: 18px; color: var(--ink);
  }
  /* Back */
  .card--back { display: flex; align-items: center; }
  .portrait {
    position: absolute; left: 150px; top: 120px;
    width: 160px; height: 160px; border-radius: 50%;
    border: 4px solid var(--green);
    padding: 4px; background: var(--card);
  }
  .portrait__fill {
    width: 100%; height: 100%; border-radius: 50%;
    background: linear-gradient(180deg, var(--photo-light) 0%, #d9c7a8 45%, var(--photo-dark) 100%);
  }
  .divider {
    position: absolute; left: 352px; top: 100px;
    width: 3px; height: 190px; background: var(--green);
  }
  .contacts {
    position: absolute; left: 376px; top: 118px;
    list-style: none;
    display: flex; flex-direction: column; gap: 16px;
  }
  .contacts__item {
    display: flex; align-items: center; gap: 16px;
    font-family: "Questrial", sans-serif;
    font-size: 15px; color: var(--grey); letter-spacing: 0.6px;
  }
  .contacts__icon {
    width: 32px; height: 32px;
    display: flex; align-items: center; justify-content: center;
    background: var(--green);
  }
  .contacts__icon--web { background: var(--orange); }
  .contacts__icon svg { width: 18px; height: 18px; }
</style>
</head>
<body>
<main class="canvas">
  <section class="card card--front" aria-label="Card front">
    <div class="brand">
      <span class="brand__mark"></span>
      <span class="brand__name">Nora Vestrel</span>
    </div>
    <p class="tagline">Smart copywriting for clever business people</p>
  </section>

  <section class="card card--back" aria-label="Card back">
    <div class="portrait">
      <div class="portrait__fill" role="img" aria-label="Portrait photo of Nora Vestrel"></div>
    </div>
    <span class="divider"></span>
    <ul class="contacts">
      <li class="contacts__item">
        <span class="contacts__icon">
          <svg viewBox="0 0 24 24"><path fill="#fff" d="M6.6 10.8a15 15 0 0 0 6.6 6.6l2.2-2.2a1 1 0 0 1 1-.25 11.4 11.4 0 0 0 3.6.57 1 1 0 0 1 1 1V20a1 1 0 0 1-1 1A17 17 0 0 1 3 4a1 1 0 0 1 1-1h3.5a1 1 0 0 1 1 1c0 1.25.2 2.45.57 3.57a1 1 0 0 1-.25 1z"/></svg>
        </span>
        0427 593 864
      </li>
      <li class="contacts__item">
        <span class="contacts__icon contacts__icon--web">
          <svg viewBox="0 0 24 24" fill="none" stroke="#fff" stroke-width="2"><circle cx="12" cy="12" r="9"/><path d="M3 12h18M12 3c3 3.5 3 14.5 0 18M12 3c-3 3.5-3 14.5 0 18"/></svg>
        </span>
        noravestrel.com.au
      </li>
      <li class="contacts__item">
        <span class="contacts__icon">
          <svg viewBox="0 0 24 24" fill="none" stroke="#fff" stroke-width="2"><rect x="3" y="6" width="18" height="12"/><path d="M3 6l9 7 9-7"/></svg>
        </span>
        nora@noravestrel.com.au
      </li>
    </ul>
  </section>
</main>
</body>
</html>
```